Branded Flyer Template Libraries Brightwater Lending

Create one-page flyer templates for equipment finance industry to provide a fast turnaround that consistent on-brand for educational and promotional flyers that can be quickly customized with partners logos. These will become a standard toolkit for marketing for use in Adobe Illustrator and editable. customer facing are business owners considering equipment financing typically used for leave behind flyers, email, and handouts. vendor facing to equipment dealers, manufacturers and sales reps who refer customers to us, typically used at trade shows, co branded flyers, and email promotions.
Requesting 1-2 flyer templates with concepts for educational, and promotional.
Brand guide and current flyers in circulation are uploaded as reference.
Look and feel
Each slider illustrates characteristics of the customer's brand and the style your logo design should communicate.

```html
<!DOCTYPE html>
<html lang="en">
<head>
<meta charset="utf-8">
<title>Brightwater Lending – Financing That Flexes With You</title>
<link rel="stylesheet" href="https://fonts.googleapis.com/css2?family=Merriweather:wght@700;900&family=Poppins:wght@400;500;600&display=swap">
<style>
:root{
  --page:#e4e5e6;
  --slate:#2d4b58;
  --green:#0f5a2b;
  --green-dark:#0e3a20;
  --leaf:#8cc46a;
  --teal:#80b0ae;
  --teal-light:#9cc3c0;
  --card:#e8e6e1;
  --card-edge:#f4f3ef;
  --lime:#a7cd7c;
  --white:#ffffff;
  --serif:'Merriweather', Georgia, serif;
  --sans:'Poppins', Arial, sans-serif;
}
*{margin:0;padding:0;box-sizing:border-box}
html,body{width:1200px;height:2534px;overflow:hidden;background:var(--page)}
.flyer{position:absolute;left:100px;top:624px;width:1000px;height:1285px;background:var(--white);overflow:hidden;box-shadow:0 10px 30px rgba(0,0,0,.12)}
.hero-photo{position:absolute;left:290px;top:0;width:710px;height:400px;
  background:linear-gradient(90deg,rgba(255,255,255,1) 0%,rgba(220,224,222,.9) 18%,#8f9f8c 35%,#4e6a4c 50%,#3c4a66 68%,#b9bdc2 85%,#d9d8d4 100%)}
.brand{position:absolute;left:42px;top:34px;display:flex;align-items:center;gap:12px}
.brand-dot{width:72px;height:72px;border-radius:50%;background:var(--green)}
.brand-name{font-family:var(--serif);font-weight:700;font-size:27px;color:var(--green);line-height:1;letter-spacing:.3px}
.brand-sub{font-family:var(--sans);font-weight:600;font-size:9px;letter-spacing:3.5px;color:var(--slate);margin-top:6px;text-align:center}
.headline{position:absolute;left:42px;top:112px;font-family:var(--serif);font-weight:900;font-size:62px;line-height:62px}
.headline .slate{color:var(--slate)}
.headline .green{color:var(--green)}
.tagline{position:absolute;left:42px;top:310px;font-family:var(--serif);font-weight:700;font-size:26px;color:var(--teal)}
.waves{position:absolute;left:0;top:330px;width:1000px;height:180px}
.intro{position:absolute;left:0;top:432px;width:1000px;text-align:center;font-family:var(--serif);font-weight:700;font-size:36px;line-height:40px}
.intro .leaf{color:var(--leaf)}
.intro .green{color:var(--green)}
.rule{display:block;margin:10px auto 0;width:150px;height:3px;background:var(--leaf)}
.intro-copy{position:absolute;left:45px;top:550px;width:910px;text-align:center;font-family:var(--sans);font-size:16px;line-height:19.5px;color:#1d1d1d}
.forest{position:absolute;left:0;top:814px;width:1000px;height:367px;
  background:radial-gradient(ellipse at 70% 30%,#1f5a33 0%,#123f24 45%,#0b2c18 100%)}
.pillar{position:absolute;top:702px;width:293px;height:126px;background:var(--card);border:5px solid var(--card-edge);outline:1px solid #d5d2cb}
.pillar-label{position:absolute;left:0;right:0;bottom:14px;text-align:center;font-family:var(--serif);font-weight:900;font-size:30px;color:var(--slate);letter-spacing:.5px}
.pillar-icon{position:absolute;top:648px;width:112px;height:112px}
.beyond{position:absolute;left:0;top:848px;width:1000px;text-align:center;font-family:var(--serif);font-weight:700;font-size:28px;color:var(--white)}
.beyond .leaf{color:var(--leaf)}
.beyond-copy{position:absolute;left:20px;top:916px;width:960px;text-align:center;font-family:var(--sans);font-size:15.5px;line-height:19px;color:var(--white)}
.checks{position:absolute;left:280px;width:700px;text-align:center;font-family:var(--sans);font-size:15px;color:var(--white);white-space:nowrap}
.checks span{margin:0 5px}
.tick{display:inline-block;width:14px;height:14px;border-radius:50%;background:var(--leaf);vertical-align:-2px;margin-right:4px;position:relative}
.tick::after{content:"";position:absolute;left:4px;top:2px;width:4px;height:7px;border:solid var(--green-dark);border-width:0 2px 2px 0;transform:rotate(45deg)}
.supplier-band{position:absolute;left:0;top:1110px;width:1000px;height:72px;background:var(--white)}
.field-photo{position:absolute;left:0;top:1000px;width:390px;height:182px}
.pill{position:absolute;left:352px;top:1078px;width:584px;height:42px;border-radius:21px;background:var(--teal-light);text-align:center;font-family:var(--serif);font-weight:700;font-size:25px;line-height:42px;color:#2e5a5c}
.supplier-checks{position:absolute;left:380px;top:1135px;width:600px;text-align:center;font-family:var(--sans);font-size:14.5px;color:var(--slate);white-space:nowrap}
.supplier-checks span{margin:0 7px}
.supplier-checks .tick{background:var(--green)}
.supplier-checks .tick::after{border-color:var(--white)}
.contact{position:absolute;left:0;top:1181px;width:1000px;height:81px;background:var(--slate);display:flex;align-items:center;justify-content:center;gap:26px;font-family:var(--sans);font-size:23px;color:var(--white)}
.contact .item{display:flex;align-items:center;gap:8px}
.contact .phone{font-weight:600}
.lime-strip{position:absolute;left:0;top:1262px;width:1000px;height:23px;background:var(--lime)}
</style>
</head>
<body>
<main class="flyer">
  <div class="hero-photo" role="img" aria-label="Photo of a farmer in a plaid shirt checking a tablet beside a pickup truck near grain silos at sunrise"></div>

  <div class="brand">
    <div class="brand-dot"></div>
    <div>
      <div class="brand-name">BRIGHTWATER LENDING</div>
      <div class="brand-sub">— EQUIPMENT FINANCE —</div>
    </div>
  </div>

  <h1 class="headline"><span class="slate">Financing</span><br><span class="green">That Flexes</span><br><span class="slate">With You</span></h1>
  <div class="tagline">let’s partner</div>

  <svg class="waves" viewBox="0 0 1000 180" preserveAspectRatio="none" aria-hidden="true">
    <path d="M0 40 C200 0 420 -5 700 30 L700 60 C420 40 200 55 0 110 Z" fill="#2d4b58"/>
    <path d="M0 110 C250 30 600 15 1000 55 L1000 140 C800 100 600 95 500 98 C300 100 140 120 0 150 Z" fill="#80b0ae"/>
    <path d="M700 100 C850 105 960 130 1000 175 L1000 140 C930 112 820 100 700 100 Z" fill="#e3e2dc"/>
    <path d="M0 150 C140 120 300 100 500 98 C300 108 140 130 0 180 Z" fill="#ffffff"/>
  </svg>

  <div class="intro">
    <div class="leaf">Here to Listen,</div>
    <div class="green">as a Partner Who Gets It.</div>
    <span class="rule"></span>
  </div>

  <p class="intro-copy">Here at Brightwater Lending, our financial experts truly believe that you’re worth the time it takes to get the perfect financing in order. Regardless of your equipment needs, our team will take the time to get to know your goals so that the creative solutions we bring forward make sense to you. How do we know what it’s like? Because we have been there ourselves, from farm families to earth movers, our collective backgrounds know a thing or two about the value of large equipment. And we’re here to support the people behind the need—you and your operation.</p>

  <div class="forest" role="img" aria-label="Dark green pine forest background"></div>

  <div class="pillar" style="left:44px"><div class="pillar-label">SOLUTIONS</div></div>
  <div class="pillar" style="left:354px"><div class="pillar-label">FLEXIBILITY</div></div>
  <div class="pillar" style="left:663px"><div class="pillar-label">SUPPORT</div></div>

  <svg class="pillar-icon" style="left:135px" viewBox="0 0 112 112" aria-hidden="true">
    <circle cx="56" cy="56" r="55" fill="#0f5a2b"/><circle cx="56" cy="56" r="48" fill="none" stroke="#8cc46a" stroke-width="1"/>
    <polygon points="56,30 63,37 73,36 74,46 81,53 74,60 73,70 63,69 56,76 49,69 39,70 38,60 31,53 38,46 39,36 49,37" fill="none" stroke="#8cc46a" stroke-width="2.5"/>
    <path d="M45 54 L53 62 L68 46" fill="none" stroke="#8cc46a" stroke-width="3"/>
  </svg>
  <svg class="pillar-icon" style="left:444px" viewBox="0 0 112 112" aria-hidden="true">
    <circle cx="56" cy="56" r="55" fill="#0f5a2b"/><circle cx="56" cy="56" r="48" fill="none" stroke="#8cc46a" stroke-width="1"/>
    <g fill="none" stroke="#8cc46a" stroke-width="3">
      <path d="M56 80 V30 M48 38 L56 30 L64 38"/>
      <path d="M56 64 C56 54 44 52 36 46 M36 54 V46 H44"/>
      <path d="M56 64 C56 54 68 52 76 46 M76 54 V46 H68"/>
    </g>
  </svg>
  <svg class="pillar-icon" style="left:753px" viewBox="0 0 112 112" aria-hidden="true">
    <circle cx="56" cy="56" r="55" fill="#0f5a2b"/><circle cx="56" cy="56" r="48" fill="none" stroke="#8cc46a" stroke-width="1"/>
    <g fill="none" stroke="#8cc46a" stroke-width="2.5">
      <rect x="32" y="36" width="10" height="8"/><rect x="70" y="36" width="10" height="8"/>
      <rect x="32" y="68" width="10" height="8"/><rect x="70" y="68" width="10" height="8"/>
      <circle cx="56" cy="56" r="7"/>
      <path d="M42 40 H70 M42 72 H70 M37 44 V68 M75 44 V68"/>
      <path d="M52 56 L55 59 L60 53"/>
    </g>
  </svg>

  <div class="beyond">We Go <span class="leaf">Beyond the Numbers</span><span class="rule"></span></div>

  <p class="beyond-copy">Since 1996, Brightwater Lending has been a steady financing partner for agriculture, construction, transportation, and environmental businesses. We cut through the clutter with clear answers and honest options, building plans around your needs. From flexible payments and extended terms to creative alternatives that protect cash flow<br>and open doors to growth, our team is here to help you grow.</p>

  <div class="checks" style="top:1004px;left:200px"><span><i class="tick"></i>Customized Payment Options</span><span><i class="tick"></i>Extended Financing Terms</span></div>
  <div class="checks" style="top:1030px"><span><i class="tick"></i>Tax-Saving Solutions</span><span><i class="tick"></i>Maintain Liquidity</span><span><i class="tick"></i>Fast Application with Dedicated Support</span></div>

  <div class="supplier-band"></div>
  <svg class="field-photo" viewBox="0 0 390 182" aria-hidden="false" role="img" aria-label="Photo of a farmer with a phone standing in a cornfield at sunset">
    <defs>
      <radialGradient id="fieldGlow" cx="0.75" cy="0.55" r="0.8">
        <stop offset="0" stop-color="#f3e7b8"/>
        <stop offset="0.35" stop-color="#7e9a5a"/>
        <stop offset="1" stop-color="#2a4424"/>
      </radialGradient>
    </defs>
    <path d="M0 40 C90 0 240 -5 330 60 C360 90 380 140 390 182 H0 Z" fill="url(#fieldGlow)" stroke="#ffffff" stroke-width="3"/>
  </svg>

  <div class="pill">Empowering Suppliers Supporting Doors</div>
  <div class="supplier-checks"><span><i class="tick"></i>Provide a Smooth Lending Experience</span><span><i class="tick"></i>Financing for Hardworking Buyers</span></div>

  <footer class="contact">
    <div class="item">
      <svg width="20" height="20" viewBox="0 0 20 20" aria-hidden="true"><g fill="none" stroke="#a7cd7c" stroke-width="1.5"><circle cx="10" cy="10" r="8"/><ellipse cx="10" cy="10" rx="3.5" ry="8"/><path d="M2 10 H18 M3.5 6 H16.5 M3.5 14 H16.5"/></g></svg>
      brightwaterlending.com
    </div>
    <div class="item">
      <svg width="20" height="16" viewBox="0 0 20 16" aria-hidden="true"><g fill="none" stroke="#a7cd7c" stroke-width="1.5"><rect x="1" y="2" width="18" height="12"/><path d="M1 2 L10 9 L19 2"/></g></svg>
      hello@brightwaterlending.com
    </div>
    <div class="item phone">
      <svg width="20" height="22" viewBox="0 0 20 22" aria-hidden="true"><path d="M5 1 L8 6 L6 8 C7 12 9 15 12 17 L14 15 L19 18 L16 21 C8 20 2 12 2 4 Z" fill="#a7cd7c"/></svg>
      (800) 555-0148
    </div>
  </footer>
  <div class="lime-strip"></div>
</main>
</body>
</html>
```